Painting Company Business Card

Brightwell Painting needs a new business card. See attachments for our logo and current card as an example.
We want to utilize the same colors in the logo, and keep all the information that is currently on it. Just need an updated and modern design.
We are open to loosing the Association Logos if it means a better design.
We are also entertaining a spot for a picture of a headshot of the person listed on the card. Head shot can be finished later.

```html
<!DOCTYPE html>
<html lang="en">
<head>
<meta charset="utf-8">
<title>Brightwell Painting – Business Card</title>
<link rel="stylesheet" href="https://fonts.googleapis.com/css2?family=Roboto:wght@400;500;700&display=swap">
<style>
  :root {
    --stage: #2a2a2a;
    --paper: #ffffff;
    --olive: #3a4330;
    --maroon: #6b3b36;
    --ink-grey: #555555;
    --white: #ffffff;
  }
  * { box-sizing: border-box; margin: 0; padding: 0; }
  html, body {
    width: 1125px;
    height: 1200px;
    overflow: hidden;
    background: var(--stage);
    font-family: "Roboto", Arial, sans-serif;
  }
  .card {
    position: absolute;
    left: 156px;
    width: 825px;
    height: 470px;
    border-radius: 24px;
    overflow: hidden;
  }
  .card--front { top: 106px; background: var(--paper); }
  .card--back { top: 639px; background: var(--maroon); }

  .brand-name {
    position: absolute;
    font-weight: 700;
    line-height: 1.05;
    letter-spacing: 0.5px;
    text-transform: uppercase;
  }
  .card--front .brand-name {
    right: 52px;
    top: 58px;
    font-size: 46px;
    color: var(--olive);
    text-align: right;
  }
  .card--back .brand-name {
    left: 46px;
    top: 245px;
    font-size: 52px;
    color: var(--white);
  }

  .contact-block { position: absolute; left: 51px; top: 320px; }
  .person-name {
    font-size: 30px;
    font-weight: 700;
    color: var(--olive);
    letter-spacing: 0.5px;
  }
  .person-title {
    margin-top: 8px;
    font-size: 21px;
    font-weight: 500;
    color: var(--maroon);
  }
  .contact-line {
    margin-top: 12px;
    font-size: 19px;
    color: var(--ink-grey);
  }

  .services {
    position: absolute;
    left: 57px;
    top: 393px;
    width: 595px;
    padding: 7px 9px;
    border-top: 1px solid var(--white);
    border-bottom: 1px solid var(--white);
    font-size: 19px;
    color: var(--white);
    white-space: nowrap;
    letter-spacing: -0.2px;
  }
</style>
</head>
<body>
  <section class="card card--front">
    <div class="brand-name">Brightwell<br>Painting</div>
    <div class="contact-block">
      <div class="person-name">DANIEL HARPER</div>
      <div class="person-title">QUALITY MANAGER</div>
      <div class="contact-line">262-555-0148 | daniel.brightwellpainting.com brightwellpainting.com</div>
    </div>
  </section>

  <section class="card card--back">
    <div class="brand-name">Brightwell<br>Painting</div>
    <div class="services">EXTERIOR PAINTING • INTERIOR PAINTING • CARPENTRY • DRYWELL</div>
  </section>
</body>
</html>
```